Wedding Expo Flyer Design

Flyer : 216mm x 139mm
We are looking to design a double sided flyer to hand out at a wedding expo we are advertising at. These fliers need to look professional and elegant, and make good use of the space on the flyer, without looking cluttered.

On one side will be advertising a deal we are offering and a voucher code to enter on our website, “Now here’s something to smile about!” “Exclusive to The Vows and Lace Fair! Book now and pay only $199 for our most popular treatment (normal price $599). Bring your partner or a friend and pay only $150 each!” Flier should include a photo of a smiling bride and groom.

On the other side of the flier we would like to tell our customers who we are, and what we do and include our logo and a design/photo.

“Pearlcrest Dental is a speciality teeth whitening clinic run by qualified practitioners. We use a revolutionary low sensitivity whitening gel meaning our treatments are fast, painless and results are guaranteed! For more information and to read some our patient testimonials please visit our website - www.pearlcrestdental.co.nz”

Located 48 Maple Crescent, Westvale or we offer a mobile service.

Fully qualified practitioners, KTRPQB (Aotearoa Oral Aesthetics Practitioners Guild) registered (include small logo)

Our phone number is 0800 GLOSSY

Target Market(s)

Male and female aged 20-39 attending a wedding/wedding expo

Industry/Entity Type

Advertising

Requirements
Must have
• Must include our logo and KTRPQB logo on the informative side of the flyer.
Nice to have
• Bride and groom on deal side of flyer. European bride & Groom.

```html
<!DOCTYPE html>
<html lang="en">
<head>
<meta charset="utf-8">
<title>Pearlcrest Dental – Vows and Lace Fair Flyer</title>
<link href="https://fonts.googleapis.com/css2?family=Arimo:wght@400;700&display=swap" rel="stylesheet">
<style>
  :root {
    --navy: #0f4677;
    --navy-text: #1b4a78;
    --sky: #4aa7dc;
    --price-blue: #58b4e4;
    --grey: #b9bbbf;
    --badge: #ffffff;
    --deco: #dfe9f2;
    --white: #ffffff;
    --ink: #1f3f63;
  }
  * { margin: 0; padding: 0; box-sizing: border-box; }
  html, body { width: 837px; height: 1200px; overflow: hidden; background: var(--white); }
  .flyer {
    position: relative;
    width: 837px;
    height: 1200px;
    overflow: hidden;
    font-family: "Arimo", Arial, sans-serif;
    background: var(--white);
  }
  .flyer-shapes { position: absolute; inset: 0; }
  .brand-name {
    position: absolute;
    top: 114px;
    left: 0;
    width: 837px;
    text-align: center;
    font-size: 74px;
    font-weight: 700;
    color: var(--navy);
    letter-spacing: -1px;
  }
  .headline {
    position: absolute;
    top: 262px;
    left: 466px;
    width: 356px;
    text-align: center;
    font-size: 43px;
    font-weight: 400;
    line-height: 1.4;
    color: var(--navy-text);
  }
  .offer { position: absolute; color: var(--white); font-weight: 400; }
  .offer-normal { top: 368px; left: 66px; width: 330px; font-size: 34px; line-height: 52px; }
  .offer-normal .price { font-size: 58px; line-height: 52px; margin-left: 8px; }
  .offer-exclusive { top: 586px; left: 72px; width: 360px; font-size: 28px; line-height: 44px; }
  .offer-exclusive .price { display: block; font-size: 58px; line-height: 66px; }
  .price { color: var(--price-blue); }
  .offer-partner { top: 880px; left: 61px; width: 380px; font-size: 30px; line-height: 44px; }
  .offer-partner .price-each { font-size: 60px; line-height: 62px; color: var(--white); }
  .offer-partner .price-each small { font-size: 38px; }
  .phone {
    position: absolute;
    top: 1090px;
    left: 60px;
    width: 367px;
    text-align: right;
    color: var(--white);
    font-size: 29px;
    line-height: 36px;
  }
  .address {
    position: absolute;
    top: 1063px;
    left: 456px;
    width: 358px;
    text-align: right;
    color: var(--ink);
    font-size: 21px;
    line-height: 1.35;
  }
  .address-label, .address-street { display: block; }
  .address-street { margin-bottom: 10px; }
</style>
</head>
<body>
<main class="flyer">
  <svg class="flyer-shapes" width="837" height="1200" viewBox="0 0 837 1200">
    <defs>
      <linearGradient id="photoTone" x1="0" y1="0" x2="1" y2="1">
        <stop offset="0" stop-color="#f1ece8"/>
        <stop offset="0.5" stop-color="#d6b7a4"/>
        <stop offset="1" stop-color="#2b2a2e"/>
      </linearGradient>
      <linearGradient id="insetTone" x1="0" y1="0" x2="1" y2="0">
        <stop offset="0" stop-color="#e8e3e0"/>
        <stop offset="1" stop-color="#c99e86"/>
      </linearGradient>
    </defs>

    <path class="top-band" d="M0,0 H837 V22 C620,55 330,110 0,112 Z" fill="var(--navy)"/>
    <path class="top-accent" d="M230,108 C450,92 650,40 837,18 V52 C650,56 450,100 230,108 Z" fill="var(--sky)"/>

    <path class="partner-panel" d="M20,772 C160,752 330,775 470,870 V1200 H20 Z" fill="var(--sky)"/>
    <path class="contact-panel" d="M441,862 C560,880 700,870 837,848 V1200 H441 Z" fill="var(--grey)"/>

    <path class="offer-panel" d="M27,297 V842 C160,815 300,820 444,880 V382 Q444,297 360,297 Z" fill="var(--navy)"/>

    <rect class="couple-photo" x="444" y="474" width="393" height="386" fill="url(#photoTone)" role="img" aria-label="Photo of a smiling bride in a veil and groom in a dark suit"/>

    <ellipse class="inset-photo" cx="628" cy="834" rx="112" ry="58" fill="url(#insetTone)" stroke="var(--navy)" stroke-width="8" transform="rotate(-12 628 834)" role="img" aria-label="Small photo of a second smiling wedding couple"/>

    <circle cx="404" cy="522" r="22" fill="var(--deco)" role="img" aria-label="Small cartoon tooth with toothbrush"/>
    <circle cx="300" cy="766" r="22" fill="var(--deco)" role="img" aria-label="Small cartoon tooth with magnifier"/>
    <circle cx="398" cy="1012" r="24" fill="var(--deco)" role="img" aria-label="Small cartoon tooth with toothpaste cap"/>

    <rect class="registration-badge" x="642" y="900" width="175" height="132" rx="10" fill="var(--badge)" role="img" aria-label="Registration badge"/>
  </svg>

  <div class="brand-name">Pearlcrest Dental</div>

  <h1 class="headline">Now here’s something to smile about!</h1>

  <p class="offer offer-normal">Our most popular treatment normal price<span class="price">$599</span></p>

  <p class="offer offer-exclusive">Exclusive to The Vows and Lace Fair! Book now and pay only <span class="price">$199</span></p>

  <p class="offer offer-partner">Bring your partner<br>or a friend and pay only<br><span class="price-each">$150 <small>each!</small></span></p>

  <p class="phone">Free Call 0800 GLOSSY<br>456 779</p>

  <p class="address">
    <span class="address-label">Address</span>
    <span class="address-street">48 Maple Crescent in Westvale</span>
    If visiting our clinic doesn't suit you we also offer a mobile service.
  </p>
</main>
</body>
</html>
```